Bluestone Advisory & Mgmt - Professional Business Cards

Hi!

I am a Real Estate Developer and Construction Consultant.

I have a lot of inspiration from previous designs and would be open to using the attached Designs as a starting point. I would like to see these styles incorporated into your designs.

I really need professional business card to go with it that includes my important info.

Look forward to seeing your designs!.

Target Market(s)

My Target market are building owners, lawyers, consultants.

Industry/Entity Type

Real Estate Development

Contact Information for Business Card

My Name: Dorian Pelkey
My Title: Principle
Company Name: Bluestone Advisory & Mgmt, LLC
Address: 348 West 71st Street, 9th FL New York, NY 10010
Mobile: 917.806.3971
Website: bam-hvx.example

Font styles to use
Serif
Sans Serif

Colors

Designer to choose colors to be used in the design.

Requirements
Must have
• Must incorporate the logo attached or have new that looks similar.
• Must use professional font that will be seen and judged by wealthy land owners and developers.
• Must incorporate some of the color green.
Should not have
• Photo's or pictures of people or buildings of any kind.

```html
<!DOCTYPE html>
<html lang="en">
<head>
<meta charset="utf-8">
<title>Bluestone Advisory &amp; Mgmt - Business Cards</title>
<link href="https://fonts.googleapis.com/css2?family=Roboto:wght@400;700;900&family=Raleway:wght@400;500&family=Open+Sans:wght@400&display=swap" rel="stylesheet">
<style>
  :root{
    --peach:#fddcb8;
    --paper:#ffffff;
    --stone:#9d9391;
    --green:#4bb574;
    --ink-light:#ffffff;
  }
  *{margin:0;padding:0;box-sizing:border-box}
  html,body{width:996px;height:1200px;overflow:hidden;background:var(--peach)}
  .sheet{position:relative;width:996px;height:1200px}
  .card{position:absolute;left:24px;width:951px;height:569px;background:var(--paper);overflow:hidden}
  .card--front{top:19px}
  .card--back{top:613px}
  .card__art{position:absolute;inset:0;width:951px;height:569px}
  .company-line{position:absolute;left:63px;top:64px;font-family:'Roboto',sans-serif;font-size:47px;font-weight:400;letter-spacing:.3px;color:var(--stone);white-space:nowrap}
  .company-line strong{color:var(--green);font-weight:900}
  .brand-name{position:absolute;font-family:'Raleway',sans-serif;font-weight:500;color:var(--green);line-height:1.02}
  .card--front .brand-name{left:63px;top:170px;font-size:66px}
  .card--back .brand-name{left:0;right:0;top:196px;text-align:center;font-size:72px}
  .holder{position:absolute;left:611px;top:256px;color:var(--ink-light);font-family:'Roboto',sans-serif}
  .holder__name{font-size:40px;font-weight:900;line-height:1.1}
  .holder__title{font-family:'Open Sans',sans-serif;font-size:26px;margin-top:2px}
  .address,.contacts{position:absolute;color:var(--ink-light);font-family:'Open Sans',sans-serif;font-size:25px;line-height:34px}
  .address{left:611px;top:404px;font-style:normal}
  .contacts{left:63px;top:438px}
  .contacts li{list-style:none;display:flex;align-items:center;gap:6px}
  .contacts svg{width:22px;height:22px}
</style>
</head>
<body>
<main class="sheet">
  <section class="card card--front">
    <svg class="card__art" viewBox="0 0 1125 673">
      <rect role="img" aria-label="Grey skyline backdrop area" fill="var(--stone)" x="0" y="290" width="1125" height="383"/>
      <rect fill="var(--paper)" x="52" y="150" width="446" height="294"/>
      <line x1="698" y1="303" x2="698" y2="396" stroke="var(--ink-light)" stroke-width="3"/>
      <polygon fill="var(--ink-light)" points="680,350 698,336 698,364"/>
    </svg>
    <h1 class="company-line"><strong>BLUESTONE</strong> ADVISORY &amp; MGMT, LLC</h1>
    <p class="brand-name">Bluestone<br>Advisory</p>
    <div class="holder">
      <p class="holder__name">Dorian Pelkey</p>
      <p class="holder__title">Principle</p>
    </div>
    <address class="address">348 West 71st Street<br>9th FL New York<br>NY 10010</address>
    <ul class="contacts">
      <li><svg viewBox="0 0 24 24" fill="none" stroke="#fff" stroke-width="1.6"><rect x="6" y="2" width="12" height="20" rx="2" transform="rotate(-12 12 12)"/></svg>: 917.806.3971</li>
      <li><svg viewBox="0 0 24 24" fill="none" stroke="#fff" stroke-width="1.6"><circle cx="12" cy="12" r="9"/><ellipse cx="12" cy="12" rx="4" ry="9"/><line x1="3" y1="12" x2="21" y2="12"/><line x1="5" y1="7" x2="19" y2="7"/><line x1="5" y1="17" x2="19" y2="17"/></svg>: bam-hvx.example</li>
    </ul>
  </section>

  <section class="card card--back">
    <svg class="card__art" viewBox="0 0 1125 673" aria-hidden="true">
      <line x1="0" y1="322" x2="320" y2="322" stroke="var(--green)" stroke-width="14"/>
      <line x1="805" y1="322" x2="1125" y2="322" stroke="var(--green)" stroke-width="14"/>
    </svg>
    <p class="brand-name">Bluestone<br>Advisory</p>
  </section>
</main>
</body>
</html>
```